plumvex stationary business card and letterhead

THIS PROJECT IS TO DESIGN A BUSINESS CARD DOUBLE SIDES .

Reason: I AM WAITING FOR TEVISH SUBMISION

Industry/Entity Type

Business

Font styles to use

```html
<!DOCTYPE html>
<html lang="en">
<head>
<meta charset="UTF-8">
<title>Plumvex Stationery – Letterhead and Business Card</title>
<link rel="stylesheet" href="https://fonts.googleapis.com/css2?family=Inter:wght@400;600;700&display=swap">
<style>
  :root {
    --backdrop: #dcdcdc;
    --paper: #ffffff;
    --brand-orange: #f15a2b;
    --brand-blue: #33309a;
    --pattern-tint: #fde1d8;
    --pattern-fade: #fff4f0;
    --card-edge: #c9c9c9;
    --text-light: #ffffff;
  }
  * { box-sizing: border-box; margin: 0; padding: 0; }
  html, body {
    width: 1200px;
    height: 900px;
    overflow: hidden;
    background: var(--backdrop);
    font-family: "Inter", Arial, sans-serif;
  }
  .stage { position: relative; width: 1200px; height: 900px; }

  /* Letterhead */
  .letterhead {
    position: absolute;
    left: 293px; top: 16px;
    width: 615px; height: 869px;
    background: var(--paper);
  }
  .letterhead__pattern {
    position: absolute;
    left: 0; top: 0;
    width: 100%; height: 67px;
    background: linear-gradient(180deg, var(--pattern-tint) 0%, var(--pattern-fade) 100%);
  }
  .letterhead__brand-tab {
    position: absolute;
    right: 0; top: 36px;
    width: 156px; height: 31px;
    background: var(--brand-blue);
    border-top-left-radius: 16px;
    display: flex; align-items: center;
    padding-left: 25px;
  }
  .letterhead__brand-name {
    color: var(--text-light);
    font-weight: 600;
    font-size: 25px;
    letter-spacing: -0.2px;
    line-height: 1;
  }
  .letterhead__footer {
    position: absolute;
    left: 0; bottom: 0;
    width: 100%; height: 47px;
    background: var(--brand-orange);
    padding: 9px 0 0 30px;
    color: var(--text-light);
    font-size: 9px;
    line-height: 11px;
  }

  /* Business card */
  .business-card {
    position: absolute;
    left: 545px; top: 343px;
    width: 270px; height: 152px;
    background: var(--paper);
    border: 1px solid var(--card-edge);
    border-top-left-radius: 26px;
    overflow: hidden;
  }
  .business-card__pattern {
    position: absolute;
    left: 0; top: 0;
    width: 100%; height: 45px;
    background: linear-gradient(180deg, var(--pattern-tint) 0%, var(--pattern-fade) 100%);
  }
  .business-card__brand-tab {
    position: absolute;
    right: 0; top: 24px;
    width: 106px; height: 21px;
    background: var(--brand-blue);
    border-top-left-radius: 11px;
    display: flex; align-items: center;
    padding-left: 15px;
  }
  .business-card__brand-name {
    color: var(--text-light);
    font-weight: 600;
    font-size: 16px;
    line-height: 1;
  }
  .business-card__body {
    position: absolute;
    left: 0; top: 45px;
    width: 100%; height: 106px;
    background: var(--brand-orange);
    color: var(--text-light);
    padding: 4px 0 0 23px;
  }
  .business-card__name {
    font-weight: 700;
    font-size: 9px;
    line-height: 11px;
  }
  .business-card__contact {
    position: absolute;
    left: 23px; top: 65px;
    font-size: 9px;
    line-height: 11px;
  }
</style>
</head>
<body>
  <main class="stage">
    <section class="letterhead" aria-label="Plumvex letterhead">
      <div class="letterhead__pattern" role="img" aria-label="Soft peach pattern of fruit and vegetable silhouettes"></div>
      <div class="letterhead__brand-tab">
        <span class="letterhead__brand-name">Plumvex</span>
      </div>
      <footer class="letterhead__footer">
        <p>Tel: 123456789</p>
        <p>Adres: Lorem ipsum / dolor sit amet 1234</p>
      </footer>
    </section>

    <section class="business-card" aria-label="Plumvex business card">
      <div class="business-card__pattern" role="img" aria-label="Soft peach pattern of fruit and vegetable silhouettes"></div>
      <div class="business-card__brand-tab">
        <span class="business-card__brand-name">Plumvex</span>
      </div>
      <div class="business-card__body">
        <p class="business-card__name">Name Surname</p>
        <div class="business-card__contact">
          <p>Tel: 123456789</p>
          <p>Adres: Lorem ipsum / dolor sit amet 1234</p>
        </div>
      </div>
    </section>
  </main>
</body>
</html>
```